Business Card Design Project

I need a new business card design for my building/development company: Kestrel Ridge Builders.

We specialise in small sub-divisions, multi-story developments and new house builds.
We handle the whole process from concept stage right throught to a fully developed property.
Updates

Target Market(s)

people looking to develop their property and need help. New property buyers

Industry/Entity Type

House

Requirements
Must have
• My logo on both sides:
Side 1: Logo taking up whole side as per old card but with a color/style change.

Side 2: Contact page: include logo but the rest just surprise me!

All contact details will be: (and need to be changable for each employee) I'll inform you of specifics before printing.

Name Surname
Position ie. Managing director
M: insert mobile
E: insert email
P.O. Box 518, Ashwell, Vic, 3094
www.kestrelridgebuilders.com.au

Nice to have
• Colors i'd like: (not necessarily all but this is the basic idea)

Black, blue, grey, silver, white

```html
<!DOCTYPE html>
<html lang="en">
<head>
<meta charset="utf-8">
<title>Kestrel Ridge Builders – Business Card</title>
<link rel="stylesheet" href="https://fonts.googleapis.com/css2?family=Quicksand:wght@300;400&family=Questrial&display=swap">
<style>
  :root {
    --page-bg: #e4e6e9;
    --blue-light: #a9d8f5;
    --blue-mid: #45a6e0;
    --blue-deep: #1f8ccf;
    --charcoal: #2c2c2d;
    --charcoal-light: #4a4a4b;
    --charcoal-dark: #1e1e1f;
    --ink: #1b2430;
    --white: #ffffff;
    --silver: #d3d7dc;
  }
  * { box-sizing: border-box; margin: 0; padding: 0; }
  html, body {
    width: 1067px;
    height: 1200px;
    overflow: hidden;
    background: var(--page-bg);
  }
  .sheet {
    width: 1067px;
    height: 1200px;
    display: flex;
    justify-content: center;
    align-items: center;
    gap: 64px;
  }
  .card {
    position: relative;
    width: 420px;
    height: 690px;
    overflow: hidden;
    box-shadow: 0 14px 34px rgba(0, 0, 0, 0.22);
  }
  .edge-strip {
    position: absolute; left: 0; top: 0; bottom: 0; width: 26px;
  }
  .texture {
    position: absolute; left: 26px; top: 0; right: 0; bottom: 0;
  }

  /* Front: contact side */
  .card--front {
    background: radial-gradient(circle at 40% 40%, var(--blue-light) 0%, var(--blue-mid) 38%, var(--blue-deep) 80%);
  }
  .card--front .edge-strip {
    background: linear-gradient(90deg, var(--charcoal-dark), var(--charcoal-light) 60%, var(--charcoal));
  }
  .card--front .texture {
    background: radial-gradient(circle at 35% 40%, rgba(255,255,255,0.12), rgba(0,60,110,0.08) 70%);
  }
  .person {
    position: absolute; left: 64px; top: 232px;
  }
  .person__name {
    font-family: "Quicksand", sans-serif;
    font-weight: 400;
    font-size: 44px;
    line-height: 1;
    color: var(--white);
    letter-spacing: 0.5px;
  }
  .person__role {
    font-family: "Questrial", sans-serif;
    font-size: 15px;
    color: var(--ink);
    margin-top: 6px;
  }
  .contact {
    position: absolute; left: 64px; top: 474px;
    font-family: "Questrial", sans-serif;
    font-size: 17px;
    line-height: 28px;
    color: var(--ink);
  }
  .contact__brand {
    display: flex; align-items: center; gap: 8px;
    margin-bottom: 2px;
  }
  .contact__mark {
    width: 16px; height: 16px;
    background: var(--ink);
  }
  .contact__company { font-size: 18px; font-weight: 700; }
  .contact__light { color: var(--white); }

  /* Back: logo side */
  .card--back {
    background: radial-gradient(circle at 55% 52%, #5a5a5b 0%, var(--charcoal) 55%, var(--charcoal-dark) 100%);
  }
  .card--back .edge-strip {
    background: linear-gradient(180deg, var(--blue-deep), var(--blue-light) 50%, var(--blue-mid));
  }
  .card--back .texture {
    background: radial-gradient(circle at 55% 50%, rgba(255,255,255,0.06), rgba(0,0,0,0.1) 80%);
  }
  .brand {
    position: absolute; left: 26px; right: 0; top: 392px;
    display: flex; flex-direction: column; align-items: center;
  }
  .brand__row { display: flex; align-items: center; gap: 12px; }
  .brand__mark {
    width: 26px; height: 26px;
    background: var(--silver);
  }
  .brand__name {
    font-family: "Questrial", sans-serif;
    font-size: 30px;
    color: var(--silver);
    white-space: nowrap;
  }
  .brand__tagline {
    font-family: "Questrial", sans-serif;
    font-size: 15px;
    color: var(--silver);
    margin-top: 4px;
    letter-spacing: 0.3px;
  }
</style>
</head>
<body>
<main class="sheet">
  <section class="card card--front" aria-label="Card front, contact details">
    <div class="edge-strip"></div>
    <div class="texture" role="img" aria-label="Faint repeating brand-mark pattern over blue"></div>
    <div class="person">
      <p class="person__name">name surname</p>
      <p class="person__role">Managing director</p>
    </div>
    <div class="contact">
      <div class="contact__brand">
        <span class="contact__mark"></span>
        <span class="contact__company">Kestrel Ridge Builders</span>
      </div>
      <p>P.O. Box 518, Ashwell, Vic, 3094</p>
      <p>M. phone: 0198 765 432</p>
      <p class="contact__light">INFO@kestrelridgebuilders.com.au</p>
      <p class="contact__light">www.kestrelridgebuilders.com.au</p>
    </div>
  </section>

  <section class="card card--back" aria-label="Card back, company name">
    <div class="edge-strip"></div>
    <div class="texture" role="img" aria-label="Faint repeating brand-mark pattern over charcoal"></div>
    <div class="brand">
      <div class="brand__row">
        <span class="brand__mark"></span>
        <span class="brand__name">Kestrel Ridge Builders</span>
      </div>
      <p class="brand__tagline">renovation-construction-development</p>
    </div>
  </section>
</main>
</body>
</html>
```